Corporate Design für Steuerkanzlei
Zielgruppe
Wir sind eine Steuerkanzlei im (ländlichen) Neustadt an der Donau, die seit über 30 Jahren von Herrn Konrad (Vater) Wimmler geführt wird. Mit Einstieg durch Herrn Felix (Sohn) Wimmler haben wir die Wimmler Steuerberatungsgellschaft mbH gegründet und suchen deshalb ein neues Kanzleilogo / Geschäftspapiere. Wir betreuen/beraten kleine Unternehmen und Privatpersonen aus der Region und haben derzeitig 14 Angestellte.
Aufgabenstellung
Das Design sollte in erster Linie seriös und nicht verspielt wirken. Einer vertrauensvollen Steuerberaterungskanzlei entsprechend. Dennoch sind wir auch für eine moderne Gestaltung offen.

```html
<!DOCTYPE html>
<html lang="de">
<head>
<meta charset="utf-8">
<title>Wimmler Steuerberatungsgesellschaft – Geschäftsausstattung</title>
<link rel="stylesheet" href="https://fonts.googleapis.com/css2?family=Oswald:wght@300;400;500&family=Open+Sans:wght@400;700&display=swap">
<style>
  :root {
    --teal: #5f8089;
    --ink: #2b2f33;
    --paper: #ffffff;
    --backdrop: #e6e8ea;
    --faint: #eeeeee;
  }
  * { margin: 0; padding: 0; box-sizing: border-box; }
  html, body { width: 1200px; height: 848px; overflow: hidden; background: var(--backdrop); }
  .stage { position: relative; width: 1200px; height: 848px; }

  .sheet, .card {
    position: absolute; background: var(--paper);
    box-shadow: 0 4px 14px rgba(0,0,0,.18);
    overflow: hidden;
  }

  /* Letterhead */
  .sheet { left: 172px; top: 64px; width: 509px; height: 720px; font-family: "Open Sans", sans-serif; color: var(--ink); }
  .brand { position: absolute; display: flex; align-items: flex-start; gap: 6px; }
  .brand-mark { border: 2px solid var(--teal); flex: none; }
  .brand-name { font-family: "Oswald", sans-serif; font-weight: 500; color: var(--ink); line-height: 1; letter-spacing: .04em; }
  .brand-claim { font-family: "Oswald", sans-serif; font-weight: 300; color: var(--teal); line-height: 1.1; letter-spacing: .02em; }

  .sheet .brand { right: 32px; top: 30px; }
  .sheet .brand-mark { width: 14px; height: 14px; margin-top: 4px; }
  .sheet .brand-name { font-size: 22px; }
  .sheet .brand-claim { font-size: 7px; }

  .pattern-strip {
    position: absolute; right: 0; top: 88px; width: 62px; height: 632px;
    background: linear-gradient(90deg, rgba(238,238,238,0) 0%, var(--faint) 100%);
  }

  .sender-line { position: absolute; left: 55px; top: 112px; font-size: 5.4px; border-bottom: .6px solid var(--teal); padding-bottom: 1px; }
  .recipient { position: absolute; left: 55px; top: 130px; font-size: 8px; line-height: 10.4px; }
  .recipient .city { margin-top: 10px; }
  .subject { position: absolute; left: 55px; top: 245px; font-size: 7.8px; font-weight: 700; }
  .letter-body { position: absolute; left: 55px; top: 272px; width: 285px; font-size: 7.5px; line-height: 9.2px; }
  .letter-body p + p { margin-top: 9px; }
  .closing { position: absolute; left: 55px; top: 504px; font-size: 7.8px; }
  .signature { position: absolute; left: 54px; top: 526px; width: 108px; height: 20px; background: linear-gradient(90deg, rgba(95,128,137,.35), rgba(95,128,137,.12)); border-radius: 3px; }
  .signer { position: absolute; left: 55px; top: 555px; font-size: 7.8px; }

  .footer { position: absolute; left: 47px; top: 677px; display: flex; }
  .footer-col {
    border-left: 1px solid var(--teal); padding-left: 7px; height: 45px;
    font-family: "Oswald", sans-serif; font-weight: 400; font-size: 6.6px; line-height: 10.3px; letter-spacing: .12em;
  }
  .footer-col:nth-child(1) { width: 119px; }
  .footer-col:nth-child(2) { width: 129px; }

  /* Business card front */
  .card-front { left: 767px; top: 198px; width: 273px; height: 176px; font-family: "Oswald", sans-serif; }
  .card-front .brand { left: 22px; top: 20px; }
  .card-front .brand-mark { width: 20px; height: 20px; margin-top: 4px; }
  .card-front .brand-name { font-size: 27px; }
  .card-front .brand-claim { font-size: 9.4px; margin-top: 2px; }
  .card-pattern { position: absolute; right: 0; top: 0; width: 52px; height: 176px; background: linear-gradient(90deg, rgba(238,238,238,0), var(--faint)); }
  .contact { position: absolute; left: 72px; top: 79px; font-size: 8.4px; line-height: 11.6px; letter-spacing: .06em; color: var(--ink); font-weight: 300; }
  .contact .name { color: var(--teal); font-weight: 500; font-size: 9px; }
  .contact .address { margin-top: 3px; }
  .contact .dot { display: inline-block; width: 3px; height: 3px; background: var(--teal); vertical-align: middle; margin: 0 4px; }
  .contact .phones { margin-top: 3px; }
  .contact .label { color: var(--teal); }
  .contact .web { color: var(--teal); font-weight: 500; margin-top: 3px; }

  /* Business card back */
  .card-back { left: 765px; top: 475px; width: 276px; height: 178px; }
  .back-pattern { position: absolute; inset: 0; background: radial-gradient(ellipse at center, var(--paper) 30%, var(--faint) 100%); }
  .card-back .brand { left: 50%; top: 50%; transform: translate(-50%, -50%); align-items: center; gap: 8px; }
  .card-back .brand-mark { width: 24px; height: 24px; border-width: 3px; margin: 0; }
  .card-back .brand-name { font-size: 30px; color: var(--teal); }
</style>
</head>
<body>
<main class="stage">

  <article class="sheet" aria-label="Briefbogen">
    <div class="pattern-strip" role="img" aria-label="Dezente Fläche für das Quadratmuster am rechten Rand"></div>

    <header class="brand">
      <span class="brand-mark"></span>
      <div>
        <div class="brand-name">Wimmler</div>
        <div class="brand-claim">Steuerberatungsgesellschaft mbH</div>
      </div>
    </header>

    <div class="sender-line">Max Mustermann, Musterstr. 123, 12345 Musterstadt</div>
    <address class="recipient" style="font-style:normal">
      Martina Musterfrau<br>Musterstraße 456
      <div class="city">12345 Berlin</div>
    </address>

    <div class="subject">Quidero molore, atatur sae. Nequat,</div>
    <div class="letter-body">
      <p>Ur sit, imus, ipicatem voluptate eum re dolluptios sequosam, eum reritati am volor sapedissi quo blaboribust, sequass itasped igendi cus exerfer feruptas iusanda ndaest, qui omnis nus aut fugitinis quatur ad ullaut mostem quasperiae corem et aciatem illatin ciduntores quidis utemquam autemperae soluptiae lab illacescia solorum et fugiam ratatatus exerro blaciis samusam etur? Uga. Neque nam simi, nest, ommod essedios magnatia nossi aute nonsequam fugiaspis moluptas sed el int etur saepe nonsecatem excea noneceperrum ulligendit faccullores et lantur si ium at.Ota cuptae non ea de opta voles rem rae dolore ilia vellab isi blanis idit veribus auda alit labore desenis imenis que in con rehent, explat ped que volorum, autent, si tetur?</p>
      <p>Ihil ium restior ecepero reptistius es aborepe diatiunt dignis diciae voluptu ribearit, que nat aute et as maximus, qui blab iur aut volest, nonsequae odios doluptatiae velignimin perescia vent.<br>Pa voluptas expero corectur molest eaquid enda vidus verciis quodi te dit aliquid unturem poreper feratur? Quis aut rehenihilit et quam, eris et perorru mquamusa quo et untia volupie nisimoluptae esseribus cora doluptati doluptatur atisciumqui re pa quat aut lam solescia intiis et millabor sit odis et quos re sam, vendicientur abo. Equi totatus rest, nosam quodi omni doloriosam des ea nimpelique volo elendae dellign ihilitis solupta temporp orupta iuntia ipiste natibusapis volesedis reriori taerrup tatiberes nobitiur, sequi omnihillab id maximagnat omnimus dolo quunt, int aut earum lacit peliquunt iduciet, id que autemolum deruptati te non re.</p>
    </div>
    <div class="closing">Sincerely</div>
    <div class="signature" role="img" aria-label="Handschriftliche Unterschrift"></div>
    <div class="signer">Max Mustermann</div>

    <footer class="footer">
      <div class="footer-col">Max Mustermann<br>Musterstr. 123<br>12345 Musterstadt</div>
      <div class="footer-col">T: 010 / 123 456 789<br>F: 010 / 123 456 790<br>info@beispielfirma.de</div>
      <div class="footer-col">Musterbank GmbH<br>IBAN: DE12345677890<br>BIC: MUS940DS90</div>
    </footer>
  </article>

  <article class="card card-front" aria-label="Visitenkarte Vorderseite">
    <div class="card-pattern" role="img" aria-label="Dezente Fläche für das Quadratmuster"></div>
    <header class="brand">
      <span class="brand-mark"></span>
      <div>
        <div class="brand-name">Wimmler</div>
        <div class="brand-claim">Steuerberatungsgesellschaft mbH</div>
      </div>
    </header>
    <div class="contact">
      <div class="name">Max Mustermann</div>
      <div>Geschäftsführer</div>
      <div class="address">Musterstr. 123<span class="dot"></span>12345 Musterstadt</div>
      <div class="phones"><span class="label">T:</span> 010 / 123 456 789&nbsp;&nbsp; <span class="label">F:</span> 010 / 123 456 791</div>
      <div>info@beispielweb.de</div>
      <div class="web">www.beispielweb.de</div>
    </div>
  </article>

  <article class="card card-back" aria-label="Visitenkarte Rückseite">
    <div class="back-pattern" role="img" aria-label="Dezente Fläche für das Quadratmuster"></div>
    <div class="brand">
      <span class="brand-mark"></span>
      <span class="brand-name">Wimmler</span>
    </div>
  </article>

</main>
</body>
</html>
```